Marisella Crowe Photography

I am looking for someone to design a business card for me. I am a newborn and children's photographer. I want the card to have the proper contact information on it, but I want it to have a soft, simplistic, dreamy type of feel to attract moms. I would love to include soft colors. Maybe lavenders or pinks etc...

I have already had the logo designed and would like it incorporated into my business card.

I have uploaded a couple of the photo's I would like to use on the card. Feel free to use just one or both of them. Or however you see fit. The most important thing is for the card to have the feel i am looking for.

Thank you!

Target Market(s)

families and pregnant women looking for photography services.

Industry/Entity Type

Business

Font styles to use
Sans Serif
Other font styles liked:
• whatever fonts look light and whimsy, but easy to read

Colors
8869ae
eea4c8
86cae6
d2a4cc
e34197
86cfc6

Requirements
Must have
• www.marisellacrowephotography-example.com
www.facebook.com/marisellacrowephotography
marisella@marisellacrowephotography-example.com
555-392-1846
Should not have
• any masculine components i.e. dark colors, square boxes etc...

```html
<!DOCTYPE html>
<html lang="en">
<head>
<meta charset="utf-8">
<title>Marisella Crowe Photography – Business Card</title>
<link href="https://fonts.googleapis.com/css2?family=Quicksand:wght@400;500&display=swap" rel="stylesheet">
<style>
  :root {
    --page: #ece8ea;
    --lavender: #d2a4cc;
    --purple: #8869ae;
    --pink: #e34197;
    --soft-pink: #eea4c8;
    --sky: #86cae6;
    --mint: #86cfc6;
    --white: #ffffff;
    --ink-light: #ffffff;
  }
  * { box-sizing: border-box; margin: 0; padding: 0; }
  html, body { width: 1200px; height: 900px; overflow: hidden; }
  body {
    background: var(--page);
    font-family: "Quicksand", sans-serif;
    position: relative;
  }
  .card {
    position: absolute;
    left: 260px;
    width: 680px;
    height: 389px;
    box-shadow: 0 6px 18px rgba(80, 60, 80, 0.15);
    overflow: hidden;
  }
  .card--back { top: 40px; background: var(--lavender); }
  .card--front { top: 471px; background: var(--white); }

  .wordmark {
    position: absolute;
    color: var(--purple);
    font-weight: 500;
    white-space: nowrap;
  }
  .card--back .wordmark { top: 46px; right: 48px; font-size: 27px; }
  .card--front .wordmark { top: 56px; left: 0; right: 0; text-align: center; font-size: 32px; }

  .contact-list {
    position: absolute;
    left: 40px;
    bottom: 42px;
    list-style: none;
  }
  .contact-list li {
    display: flex;
    align-items: center;
    gap: 10px;
    height: 30px;
    color: var(--ink-light);
    font-size: 15px;
  }
  .contact-icon {
    width: 24px;
    height: 22px;
    border-radius: 4px;
    background: var(--pink);
    display: flex;
    align-items: center;
    justify-content: center;
    flex: none;
  }

  .photo-row {
    position: absolute;
    top: 130px;
    left: 0;
    right: 0;
    display: flex;
    justify-content: center;
    gap: 46px;
  }
  .photo {
    width: 92px;
    height: 92px;
    border-radius: 50%;
  }
  .photo--one { background: radial-gradient(circle at 50% 40%, #d9c3b6, #7fb8ae 80%); }
  .photo--two { background: radial-gradient(circle at 50% 40%, #f1c6b6, var(--pink) 80%); }
  .photo--three { background: radial-gradient(circle at 50% 45%, #e6dde8, #8c9fd2 85%); }
  .photo--four { background: radial-gradient(circle at 50% 45%, #e4c98f, #f3e4b5 85%); }

  .web-band {
    position: absolute;
    top: 262px;
    left: 0;
    right: 0;
    height: 62px;
    background: var(--lavender);
    display: flex;
    align-items: center;
    justify-content: center;
  }
  .web-band span {
    color: var(--purple);
    font-size: 21px;
    letter-spacing: 0.5px;
  }
</style>
</head>
<body>

<section class="card card--back" aria-label="Card back">
  <div class="wordmark">Marisella Crowe Photography</div>
  <ul class="contact-list">
    <li>
      <span class="contact-icon">
        <svg width="14" height="14" viewBox="0 0 24 24"><path d="M6.6 10.8a15 15 0 0 0 6.6 6.6l2.2-2.2a1 1 0 0 1 1-.25 11.4 11.4 0 0 0 3.6.57 1 1 0 0 1 1 1V20a1 1 0 0 1-1 1A17 17 0 0 1 3 4a1 1 0 0 1 1-1h3.5a1 1 0 0 1 1 1c0 1.25.2 2.45.57 3.57a1 1 0 0 1-.25 1z" fill="#fff"/></svg>
      </span>
      555-392-1846
    </li>
    <li>
      <span class="contact-icon">
        <svg width="15" height="11" viewBox="0 0 24 17"><rect x="1" y="1" width="22" height="15" rx="1.5" fill="none" stroke="#fff" stroke-width="2"/><path d="M1 2l11 8 11-8" fill="none" stroke="#fff" stroke-width="2"/></svg>
      </span>
      marisella@marisellacrowephotography-example.com
    </li>
    <li>
      <span class="contact-icon">
        <svg width="14" height="14" viewBox="0 0 24 24"><circle cx="10" cy="10" r="6.5" fill="none" stroke="#fff" stroke-width="2.5"/><path d="M15 15l6 6" stroke="#fff" stroke-width="3" stroke-linecap="round"/></svg>
      </span>
      www.marisellacrowephotography-example.com
    </li>
    <li>
      <span class="contact-icon"></span>
      marisellacrowephotography
    </li>
  </ul>
</section>

<section class="card card--front" aria-label="Card front">
  <div class="wordmark">Marisella Crowe Photography</div>
  <div class="photo-row">
    <div class="photo photo--one" role="img" aria-label="Portrait of a baby in a mint outfit"></div>
    <div class="photo photo--two" role="img" aria-label="Portrait of a toddler in pink"></div>
    <div class="photo photo--three" role="img" aria-label="Portrait of a young child by a window"></div>
    <div class="photo photo--four" role="img" aria-label="Portrait of a child in soft yellow light"></div>
  </div>
  <div class="web-band"><span>www.marisellacrowephotography-example.com</span></div>
</section>

</body>
</html>
```